Business cards and logo for a international shipping company called Harborline Freight LLC. We would like to incorporate the colors red and blue. We would like the theme to be nautical.

Industry/Entity Type

Business

```html
<!DOCTYPE html>
<html lang="en">
<head>
<meta charset="utf-8">
<title>Harborline Freight LLC — Business Card</title>
<link rel="stylesheet" href="https://fonts.googleapis.com/css2?family=Cinzel:wght@700&family=Raleway:wght@400&family=Roboto+Condensed:ital,wght@0,400;1,700&display=swap">
<style>
  :root {
    --bg: #e9eef2;
    --card: #ffffff;
    --teal: #1a9ca6;
    --red: #e04a2f;
    --ink: #1e1e1e;
    --grey: #444a4f;
    --wash: #e6eef8;
    --visual-light: #eef3f9;
    --visual-mid: #c7d9ec;
    --visual-deep: #9fc0de;
    --rule: #cfd6dd;
  }
  * { margin: 0; padding: 0; box-sizing: border-box; }
  html, body { width: 1200px; height: 1200px; overflow: hidden; background: var(--bg); }
  .canvas { position: relative; width: 1200px; height: 1200px; }
  .card {
    position: absolute; left: 100px; top: 290px;
    width: 1000px; height: 619px;
    background:
      linear-gradient(160deg, var(--wash) 0%, rgba(255,255,255,0) 35%),
      var(--card);
    overflow: hidden;
    box-shadow: 0 10px 30px rgba(20, 40, 60, 0.18);
  }
  .card-rules { position: absolute; left: 0; bottom: 0; width: 1000px; height: 619px; }
  .freight-visual {
    position: absolute; left: 600px; top: 160px;
    width: 400px; height: 459px;
    background: linear-gradient(180deg, var(--visual-light) 0%, var(--visual-mid) 55%, var(--visual-deep) 100%);
    -webkit-mask-image: linear-gradient(90deg, transparent 0%, #000 35%);
            mask-image: linear-gradient(90deg, transparent 0%, #000 35%);
  }
  .brand { position: absolute; left: 0; right: 0; top: 66px; text-align: center; }
  .brand-name {
    font-family: "Cinzel", "Times New Roman", serif;
    font-weight: 700; font-size: 52px; line-height: 1;
    color: var(--teal); letter-spacing: 0.5px; padding-left: 42px;
  }
  .brand-tagline {
    margin-top: 10px; padding-left: 42px;
    font-family: "Raleway", Arial, sans-serif;
    font-size: 30px; color: var(--grey); letter-spacing: 0.3px;
  }
  .person { position: absolute; left: 110px; top: 224px; }
  .person-name {
    font-family: "Roboto Condensed", Arial, sans-serif;
    font-style: italic; font-weight: 700; font-size: 48px; line-height: 1;
    color: var(--red);
  }
  .person-role {
    margin-top: 10px;
    font-family: "Roboto Condensed", Arial, sans-serif;
    font-size: 26px; color: var(--grey);
  }
  .contacts { position: absolute; left: 110px; top: 330px; list-style: none; }
  .contact {
    display: flex; align-items: center; height: 48px;
    font-family: "Roboto Condensed", Arial, sans-serif;
    font-size: 27px; color: var(--ink);
  }
  .contact svg { width: 30px; height: 30px; margin-right: 12px; flex: none; }
  .toll-free {
    position: absolute; left: 110px; top: 480px;
    font-family: "Roboto Condensed", Arial, sans-serif;
    font-style: italic; font-weight: 700; font-size: 35px;
    color: var(--teal);
  }
</style>
</head>
<body>
<div class="canvas">
  <div class="card">
    <div class="freight-visual" role="img" aria-label="Illustration of a cargo plane, container ship, delivery trucks and parcels around a globe"></div>

    <svg class="card-rules" viewBox="0 0 1000 619" aria-hidden="true">
      <g stroke="var(--rule)" stroke-width="1.5">
        <line x1="0" y1="568" x2="1000" y2="568"/>
        <line x1="0" y1="576" x2="1000" y2="576"/>
        <line x1="0" y1="584" x2="1000" y2="584"/>
        <line x1="0" y1="592" x2="1000" y2="592"/>
        <line x1="0" y1="600" x2="1000" y2="600"/>
        <line x1="0" y1="608" x2="1000" y2="608"/>
      </g>
    </svg>

    <header class="brand">
      <div class="brand-name">HARBORLINE FREIGHT LLC</div>
      <div class="brand-tagline">INTERNATIONAL SHIPPING COMPANY</div>
    </header>

    <div class="person">
      <div class="person-name">Marcus Hale</div>
      <div class="person-role">Founder/Director</div>
    </div>

    <ul class="contacts">
      <li class="contact">
        <svg viewBox="0 0 24 24" aria-hidden="true"><path fill="var(--red)" d="M7 2h3l1 5-2.5 1.5c1 3 3 5.5 6 7L16 13l5 1v3c0 2-1.5 3.5-3.5 3.5C10 20.5 3.5 14 3.5 6.5 3.5 4 5 2 7 2z"/></svg>
        555.014.0192
      </li>
      <li class="contact">
        <svg viewBox="0 0 24 24" aria-hidden="true"><text x="12" y="19" text-anchor="middle" font-family="Roboto Condensed, sans-serif" font-style="italic" font-size="22" fill="var(--red)">@</text></svg>
        contact@harborlinefreight.com
      </li>
      <li class="contact">
        <svg viewBox="0 0 24 24" aria-hidden="true"><g fill="none" stroke="var(--red)" stroke-width="1.4"><circle cx="12" cy="12" r="9"/><ellipse cx="12" cy="12" rx="4" ry="9"/><line x1="3" y1="12" x2="21" y2="12"/><line x1="4.5" y1="7.5" x2="19.5" y2="7.5"/><line x1="4.5" y1="16.5" x2="19.5" y2="16.5"/></g></svg>
        harborlinefreightllc.com
      </li>
    </ul>

    <div class="toll-free">Toll Free: 888-555-0147</div>
  </div>
</div>
</body>
</html>
```